Website for legal expungement services with button to qualify/disqualify potential clients

Larkfield Record Relief, LLC is a law firm focusing in legal expungement servcies (allowing people to erase criminal court records, police records, proseution files, etc). I want a more modern look which exudes confidence in the services. I am looking for a clean website that looks very polished. I want to keep the pages to a minimum, as I want the page not so much to answer questions, but to direct traffic to contact the law office. I would like the main focus point to be an button which would take a client through a series of questions to see if they would qualify for the services; this serves two purposes 1) to collect contact info for future marketing via email and 2) eliminate individuals who we are currently unable to help. A current theme that I have played around with are "Change so much, you'll need to reintroduce yourself" alongside a picture of a guys hand outstretched.
On the landing page, I would like a very brief and to the point explanation of what the service would be (i.e. "Leave your past in the past; expunge all your criminal records" ), followed by a list of benefits that it provides. (NB: included is a file "law post card-02" that includes the main benefits to expungement). Also included are two logo files for a more updated logo I currently use ("LRR Logo" and LRR Logo2") (NB: I'm open to revisions on this as well). Lastly, I've had two very minor 'ads' that I did ("postcard back" and "HVC Ad") that I like the idea of.

Target Market(s)

Middle/upper-middle class, mostly male, people with a criminal record or criminal accusation

Industry/Entity Type

Legal Services

Coding

Coded - Design and coding required

Requirements
Must have
• Button that attracts attention up front (possibly stand out coloring) to click to open up a series of questions to qualify/eliminate prospects, and simultaneously gather their info. Also, must be mobile friendly.

```html
<!DOCTYPE html>
<html lang="en">
<head>
<meta charset="utf-8">
<title>Larkfield Record Relief</title>
<link href="https://fonts.googleapis.com/css2?family=Cinzel:wght@400;500&family=Montserrat:ital,wght@0,400;0,500;0,600;1,500&display=swap" rel="stylesheet">
<style>
:root{
  --navy:#1f3b66;
  --navy-deep:#1c3455;
  --steel:#34547a;
  --gold:#d8a62a;
  --gold-light:#e6bb45;
  --mist:#f4f5f8;
  --line:#e2e5ea;
  --ink:#333a44;
  --muted:#6b7280;
  --white:#ffffff;
}
*{margin:0;padding:0;box-sizing:border-box}
html,body{width:1200px;height:4890px;overflow:hidden}
body{font-family:"Montserrat",sans-serif;color:var(--ink);background:var(--white);position:relative}
.serif{font-family:"Cinzel",serif}
section,header,footer{position:absolute;left:0;width:1200px;overflow:hidden}
.abs{position:absolute}
.btn{position:absolute;background:var(--gold);color:var(--white);font-weight:600;display:flex;align-items:center;justify-content:center;letter-spacing:.5px}
.heading{font-family:"Cinzel",serif;color:var(--navy);font-weight:500;letter-spacing:1px}

/* brand */
.brand{position:absolute;display:flex;align-items:center;gap:18px}
.brand-mark{border:2px solid currentColor}
.brand-name{font-family:"Cinzel",serif;font-weight:500;line-height:1.2;letter-spacing:.5px}

/* hero */
.hero{top:0;height:706px}
.hero-scene{position:absolute;inset:0;background:linear-gradient(180deg,#27548f 0%,#3d6fae 30%,#6f8fb5 52%,#8a8f8a 68%,#5c6a5a 80%,#2f3b44 100%)}
.hero-shade{position:absolute;inset:0;background:linear-gradient(180deg,rgba(20,40,80,.35),rgba(20,40,80,0) 45%)}
.nav{position:absolute;top:50px;left:564px;display:flex;gap:27px;font-size:15px;font-weight:600;color:var(--white)}
.nav .active{color:var(--gold-light)}
.hero-title{position:absolute;top:190px;width:1200px;text-align:center;color:var(--white);font-size:51px;line-height:68px;font-weight:400;font-family:"Cinzel",serif;letter-spacing:1px}

/* welcome */
.welcome{top:706px;height:709px}
.centered{position:absolute;width:1200px;text-align:center}
.welcome-title{top:70px;font-size:40px;line-height:52px}
.welcome-text{top:198px;font-size:15.5px;line-height:25px;color:var(--muted)}
.process{position:absolute;left:110px;top:344px;width:978px;height:274px;border:2px solid var(--line)}
.process-label{position:absolute;left:489px;transform:translateX(-50%);top:-16px;background:var(--white);padding:0 22px;font-size:24px;font-weight:500;color:var(--ink)}
.step{position:absolute;top:42px;width:230px;text-align:center;transform:translateX(-50%)}
.step svg{display:block;margin:0 auto}
.step h3{margin-top:22px;font-size:19px;font-weight:500;color:var(--ink)}
.step p{margin-top:14px;font-size:15px;line-height:25px;color:var(--muted)}

/* intro */
.intro{top:1415px;height:598px;background:var(--mist)}
.intro-title{left:110px;top:80px;font-size:39px;line-height:51px}
.intro-text{position:absolute;left:110px;top:254px;font-size:15px;line-height:26.5px;color:#4b5260}
.intro-frame{position:absolute;left:676px;top:58px;width:428px;height:433px;border:3px solid var(--navy)}
.intro-photo{position:absolute;left:700px;top:85px;width:430px;height:433px;background:linear-gradient(135deg,#c6ccd4 0%,#e8e4de 35%,#8aa3c4 60%,#3d4a5c 100%)}

/* benefits */
.benefits{top:2013px;height:787px;background:var(--steel)}
.benefits-title{top:80px;color:var(--white);font-size:39px}
.cell{position:absolute;width:318px;height:167px;background:var(--navy-deep);border-radius:4px;display:flex;align-items:center;padding-left:22px;gap:22px;color:var(--white);font-size:17px;line-height:27px}
.cell svg{flex:none}
.cell.brand-cell{background:var(--white);justify-content:center;padding:0;gap:16px;color:var(--navy)}

/* case types */
.types{top:2800px;height:371px}
.types-title{left:110px;top:120px;font-size:39px;line-height:51px}
.type{position:absolute;top:70px;width:230px;text-align:center;transform:translateX(-50%)}
.type-ring{width:132px;height:132px;border:2.5px solid var(--navy);border-radius:50%;margin:0 auto;display:flex;align-items:center;justify-content:center}
.type p{margin-top:24px;font-size:16px;line-height:25px;color:#4b5260}

/* testimonials */
.reviews{top:3171px;height:497px;background:var(--mist)}
.reviews-orb{position:absolute;left:-250px;top:-10px;width:720px;height:440px;border-radius:50%;background:#e9ebf0}
.reviews-arc{position:absolute;left:940px;top:350px;width:420px;height:420px;border-radius:50%;background:#f1e7d2}
.reviews-title{top:66px;font-size:39px}
.face{position:absolute;border-radius:50%;border:4px solid var(--white)}
.client-name{position:absolute;left:351px;top:378px;transform:translateX(-50%);font-size:22px;font-weight:500}
.dots{position:absolute;left:323px;top:420px;display:flex;gap:5px}
.dots span{width:8px;height:8px;border-radius:50%;background:var(--navy)}
.dots span.on{background:var(--gold)}
.quote-mark{position:absolute;left:664px;top:150px;font-family:"Cinzel",serif;font-size:110px;line-height:110px;color:var(--gold)}
.quote{position:absolute;left:668px;top:218px;font-size:21.5px;line-height:34.5px;font-style:italic;font-weight:500;color:#2e3440;white-space:nowrap}

/* contact */
.contact{top:3668px;height:652px}
.contact-title{top:72px;font-size:39px}
.field{position:absolute;border:1.5px solid #cfd4db;font-size:15px;color:#6b7280;padding:16px 18px}
.submit{left:537px;top:503px;width:126px;height:61px;font-size:16px}

/* call band */
.call{top:4320px;height:199px;background:linear-gradient(100deg,#c99a22 0%,#d8a62a 40%,#e2b844 70%,#d3a128 100%);color:var(--white);text-align:center}
.call p{position:absolute;width:1200px;top:53px;font-size:23px;font-weight:500}
.call .phone{position:absolute;width:1200px;top:100px;font-size:38px;font-weight:600;display:flex;justify-content:center;align-items:center;gap:14px}

/* footer */
.footer{top:4519px;height:371px;background:var(--white)}
.footer h4{position:absolute;top:62px;font-size:16px;font-weight:600;color:#2e3440}
.links{position:absolute;left:579px;top:106px;list-style:none;font-size:15px;line-height:27.5px;color:#4b5260}
.contact-list{position:absolute;left:758px;top:106px;list-style:none;font-size:15px;color:#4b5260}
.contact-list li{display:flex;align-items:center;gap:10px;height:47px}
.footer-rule{position:absolute;left:110px;top:283px;width:978px;height:1.5px;background:var(--line)}
.copyright{position:absolute;left:110px;top:309px;font-size:14px;color:#4b5260}
.social{position:absolute;top:295px;width:48px;height:48px;border:2px solid var(--gold);border-radius:50%}
</style>
</head>
<body>

<header class="hero">
  <div class="hero-scene" role="img" aria-label="City skyline at dusk under a deep blue sky"></div>
  <div class="hero-shade"></div>
  <div class="brand" style="left:110px;top:40px;color:var(--white)">
    <span class="brand-mark" style="width:44px;height:44px"></span>
    <span class="brand-name" style="font-size:15px">LARKFIELD RECORD<br>RELIEF</span>
  </div>
  <nav class="nav">
    <span class="active">HOME</span><span>ABOUT US</span><span>SERVICES</span><span>BENEFITS</span><span>CONTACT US</span>
  </nav>
  <h1 class="hero-title">CHANGE SO MUCH, YOU’LL<br>NEED TO REINTRODUCE YOURSELF</h1>
  <div class="btn" style="left:475px;top:346px;width:248px;height:76px;font-size:19px">CHECK ELIGIBILITY</div>
</header>

<section class="welcome">
  <h2 class="heading centered welcome-title">WELCOME TO<br>LARKFIELD RECORD RELIEF</h2>
  <p class="centered welcome-text">Larkfield Record Relief is 5-star rated firm, which has been formed with the passing of the Larkfield<br>Expungement law of 2020. It is a subdivision of the Harlow Law Group, and since its creation has<br>helped over 100 Larkfield citizens successfully expunge their criminal records.</p>
  <div class="process">
    <span class="process-label">Our Process</span>
    <div class="step" style="left:124px">
      <svg width="70" height="84" viewBox="0 0 70 84" fill="none" stroke="var(--navy)" stroke-width="2.5"><rect x="6" y="8" width="58" height="74" rx="3"/><rect x="22" y="2" width="26" height="12" rx="2"/><path d="M14 30l4 4 7-7M14 46l4 4 7-7M14 62l7 7M21 62l-7 7" stroke="var(--gold)"/><path d="M32 32h24M32 48h24M32 66h24"/></svg>
      <h3>1. Screening</h3><p>Neque porro quisq uaest,<br>qui dolorem ipsum.</p>
    </div>
    <div class="step" style="left:369px">
      <svg width="86" height="84" viewBox="0 0 86 84" fill="none" stroke="var(--navy)" stroke-width="2.5"><rect x="4" y="18" width="78" height="58" rx="4"/><rect x="34" y="6" width="18" height="16" rx="2"/><circle cx="26" cy="40" r="8"/><path d="M12 64c2-10 26-10 28 0M50 40h22M50 50h14"/><circle cx="60" cy="62" r="12" stroke="var(--gold)"/><path d="M54 62l4 4 8-8" stroke="var(--gold)"/></svg>
      <h3>2. Verify identity</h3><p>Neque porro quisq uaest,<br>qui dolorem ipsum.</p>
    </div>
    <div class="step" style="left:612px">
      <svg width="62" height="84" viewBox="0 0 62 84" fill="none" stroke="var(--navy)" stroke-width="2.5"><path d="M4 4h38l16 16v60H4z"/><path d="M42 4v16h16"/><circle cx="30" cy="42" r="11" stroke="var(--gold)"/><path d="M38 50l10 10" stroke="var(--gold)"/></svg>
      <h3>3. Record analysis</h3><p>Neque porro quisq uaest,<br>qui dolorem ipsum.</p>
    </div>
    <div class="step" style="left:857px">
      <svg width="80" height="84" viewBox="0 0 80 84" fill="none" stroke="var(--navy)" stroke-width="2.5"><rect x="4" y="4" width="48" height="66" rx="2"/><rect x="12" y="12" width="48" height="66" rx="2" fill="#fff"/><path d="M20 26h32M20 36h32M20 46h24M20 56h18"/><circle cx="58" cy="64" r="8" stroke="var(--gold)"/><path d="M64 58l12-12M68 60l8-8" stroke="var(--gold)"/></svg>
      <h3>4. Legal services</h3><p>Neque porro quisq uaest,<br>qui dolorem ipsum.</p>
    </div>
  </div>
</section>

<section class="intro">
  <h2 class="heading abs intro-title">LEAVE YOUR PAST IN THE<br>PAST; EXPUNGE ALL YOUR<br>CRIMINAL RECORDS</h2>
  <p class="intro-text">Nemo enim ipsam voluptatem quia voluptas sit aspernaturut<br>odit aut fugit, sed quia consequuntur magni dolores eos qui<br>ratione voluptatem sequi nesciunt. Neque porro quisquaest,<br>qui dolorem ipsum quia dolor sit amet, consectetur, adipisci<br>velit, sed quia non numquam eius modi tempora incidunt ut<br>labore et dolore magnam aliquam .</p>
  <div class="btn" style="left:110px;top:444px;width:160px;height:59px;font-size:16px">READ MORE</div>
  <div class="intro-frame"></div>
  <div class="intro-photo" role="img" aria-label="Smiling man in a denim shirt working on a laptop"></div>
</section>

<section class="benefits">
  <h2 class="heading centered benefits-title">THE BENEFITS OF EXPUNGEMENT</h2>
  <div class="cell" style="left:110px;top:173px">
    <svg width="84" height="70" viewBox="0 0 84 70" fill="none" stroke="#fff" stroke-width="2.5"><rect x="22" y="4" width="56" height="32" rx="2"/><circle cx="50" cy="20" r="8"/><path d="M4 42c10-6 22-6 30 0h14c4 0 4 6 0 6H34M4 58c14 8 30 8 48-6l14-12c4-4-2-8-6-4L48 46"/></svg>
    <span>More and better<br>job opportunities<br>leading to higher<br>income</span>
  </div>
  <div class="cell" style="left:442px;top:173px">
    <svg width="80" height="84" viewBox="0 0 80 84" fill="none" stroke="#fff" stroke-width="2.5"><path d="M40 6v74M28 18l12-12 12 12M20 40v36M58 40v36"/><rect x="8" y="50" width="16" height="20" stroke-dasharray="4 4"/><rect x="54" y="46" width="16" height="20" stroke-dasharray="4 4"/></svg>
    <span>Loan qualification<br>and better loan<br>rates</span>
  </div>
  <div class="cell" style="left:771px;top:173px">
    <svg width="80" height="84" viewBox="0 0 80 84" fill="none" stroke="#fff" stroke-width="2.5"><path d="M40 6l30 12v22c0 20-14 32-30 38C24 72 10 60 10 40V18z"/><rect x="30" y="40" width="20" height="16" rx="2"/><path d="M34 40v-6a6 6 0 0 1 12 0v6"/></svg>
    <span>Protecting your<br>privacy</span>
  </div>
  <div class="cell" style="left:110px;top:353px">
    <svg width="84" height="84" viewBox="0 0 84 84" fill="none" stroke="#fff" stroke-width="2.5"><path d="M8 6h44v20M8 6v70h30"/><path d="M16 20h28M16 32h20M16 44h16"/><path d="M72 22l8 8-34 34-12 4 4-12z"/></svg>
    <span>Better education<br>opportunities</span>
  </div>
  <div class="cell brand-cell" style="left:442px;top:353px">
    <span class="brand-mark" style="width:40px;height:40px;color:var(--navy)"></span>
    <span class="brand-name" style="font-size:17px">LARKFIELD RECORD<br>RELIEF</span>
  </div>
  <div class="cell" style="left:771px;top:353px">
    <svg width="88" height="84" viewBox="0 0 88 84" fill="none" stroke="#fff" stroke-width="2.5"><rect x="26" y="6" width="22" height="30" rx="3" transform="rotate(40 37 21)"/><path d="M48 36l30 26-6 6-28-28M6 78h30M12 70h18"/></svg>
    <span>Removing the<br>stigma of having<br>a criminal record</span>
  </div>
  <div class="cell" style="left:110px;top:533px">
    <svg width="84" height="84" viewBox="0 0 84 84" fill="none" stroke="#fff" stroke-width="2.5"><path d="M6 44L42 10l36 34M16 36v42h56V36"/><rect x="24" y="50" width="14" height="28"/><rect x="46" y="50" width="18" height="14"/><path d="M55 50v14M46 57h18"/></svg>
    <span>More options for<br>housing</span>
  </div>
  <div class="cell" style="left:442px;top:533px">
    <svg width="80" height="84" viewBox="0 0 80 84" fill="none" stroke="#fff" stroke-width="2.5"><path d="M20 6h40v24a20 20 0 0 1-40 0zM20 14H8c0 14 6 20 14 20M60 14h12c0 14-6 20-14 20M40 50v16M26 78h28l-4-12H30z"/><path d="M40 14l4 8 8 1-6 6 2 8-8-4-8 4 2-8-6-6 8-1z"/></svg>
    <span>Qualifying for<br>government<br>assistance<br>programs</span>
  </div>
  <div class="cell" style="left:771px;top:533px">
    <svg width="84" height="84" viewBox="0 0 84 84" fill="none" stroke="#fff" stroke-width="2.5"><path d="M8 6h44v30M8 6v72h28"/><path d="M16 20h28M16 32h20M16 44h14M14 62l4 4 6-6"/><circle cx="58" cy="60" r="18"/><path d="M64 52c-2-3-12-3-12 2s12 3 12 9-10 5-12 2M58 46v28"/></svg>
    <span>Lower insurance<br>premiums</span>
  </div>
</section>

<section class="types">
  <h2 class="heading abs types-title">WHAT TYPES OF<br>CASES QUALIFY</h2>
  <div class="type" style="left:570px">
    <div class="type-ring"><svg width="60" height="66" viewBox="0 0 60 66" fill="none" stroke="var(--gold)" stroke-width="2.5"><path d="M6 4h32l12 12v46H6z"/><path d="M14 26h26M14 36h26M14 46h16"/><circle cx="46" cy="50" r="9"/><path d="M42 46l8 8M50 46l-8 8"/></svg></div>
    <p>Criminal accusations<br>that were dismissed</p>
  </div>
  <div class="type" style="left:794px">
    <div class="type-ring"><svg width="70" height="70" viewBox="0 0 70 70" fill="none" stroke="var(--gold)" stroke-width="2.5"><path d="M35 4l31 31-31 31L4 35z"/><path d="M26 44v-8h16M36 30l6 6-6 6"/></svg></div>
    <p>Criminal cases that<br>went into a diversionary<br>Program</p>
  </div>
  <div class="type" style="left:1006px">
    <div class="type-ring"><svg width="62" height="70" viewBox="0 0 62 70" fill="none" stroke="var(--gold)" stroke-width="2.5"><path d="M31 4l26 10v20c0 18-12 28-26 32C17 62 5 52 5 34V14z"/><path d="M22 44V26M28 44V22M34 44V24M40 44V28M22 44h18"/></svg></div>
    <p>Convictions</p>
  </div>
</section>

<section class="reviews">
  <div class="reviews-orb"></div>
  <div class="reviews-arc"></div>
  <h2 class="heading centered reviews-title">WHAT OUR CLIENTS SAY</h2>
  <div class="face" role="img" aria-label="Client portrait" style="left:110px;top:198px;width:114px;height:114px;background:#d6c7b8;opacity:.75"></div>
  <div class="face" role="img" aria-label="Client portrait" style="left:178px;top:188px;width:124px;height:124px;background:#b7a595"></div>
  <div class="face" role="img" aria-label="Client portrait" style="left:478px;top:198px;width:114px;height:114px;background:#d9cfc6;opacity:.75"></div>
  <div class="face" role="img" aria-label="Client portrait" style="left:404px;top:188px;width:124px;height:124px;background:#a9a29e"></div>
  <div class="face" role="img" aria-label="Featured client portrait" style="left:262px;top:166px;width:178px;height:178px;background:linear-gradient(160deg,#e5e1dc,#b08a6a 70%,#7a5a44)"></div>
  <div class="client-name">Marta</div>
  <div class="dots"><span></span><span></span><span class="on"></span><span></span><span></span></div>
  <div class="quote-mark">“</div>
  <p class="quote">Sed ut perspiciatis unde omnis<br>iste natus error sit voluptatem accu<br>tium doloremque laudantium, totam<br>rem aperiam, eaque ipsa quae ab illo<br>inventore veritatis et quasi architecto<br>beatae vitae dicta sunt.”</p>
</section>

<section class="contact">
  <h2 class="heading centered contact-title">CONTACT US</h2>
  <div class="field" style="left:154px;top:163px;width:440px;height:53px">First Name</div>
  <div class="field" style="left:604px;top:163px;width:440px;height:53px">Last Name</div>
  <div class="field" style="left:154px;top:230px;width:440px;height:53px">Email Address</div>
  <div class="field" style="left:604px;top:230px;width:440px;height:53px">Phone Number</div>
  <div class="field" style="left:154px;top:295px;width:890px;height:163px">Message</div>
  <div class="btn submit">SUBMIT</div>
</section>

<section class="call">
  <p>To see if you qualify for expungement or for additional information, contact us</p>
  <div class="phone"><svg width="32" height="32" viewBox="0 0 24 24" fill="#fff"><path d="M6.6 10.8a15.1 15.1 0 0 0 6.6 6.6l2.2-2.2a1 1 0 0 1 1-.25 11.4 11.4 0 0 0 3.6.57 1 1 0 0 1 1 1V20a1 1 0 0 1-1 1A17 17 0 0 1 3 4a1 1 0 0 1 1-1h3.5a1 1 0 0 1 1 1c0 1.25.2 2.45.57 3.57a1 1 0 0 1-.25 1z"/></svg>555-014-2290</div>
</section>

<footer class="footer">
  <div class="brand" style="left:112px;top:96px;color:var(--navy)">
    <span class="brand-mark" style="width:48px;height:48px"></span>
    <span class="brand-name" style="font-size:22px">LARKFIELD RECORD<br>RELIEF</span>
  </div>
  <h4 style="left:579px">Quick Links</h4>
  <ul class="links"><li>Home</li><li>About us</li><li>Services</li><li>Benefits</li><li>Contact Us</li></ul>
  <h4 style="left:758px">Contact Us</h4>
  <ul class="contact-list">
    <li><svg width="12" height="16" viewBox="0 0 12 16" fill="var(--gold)"><path d="M6 0a6 6 0 0 1 6 6c0 4-6 10-6 10S0 10 0 6a6 6 0 0 1 6-6zm0 4a2 2 0 1 0 0 4 2 2 0 0 0 0-4z"/></svg>Larkfield</li>
    <li><svg width="14" height="14" viewBox="0 0 24 24" fill="var(--gold)"><path d="M6.6 10.8a15.1 15.1 0 0 0 6.6 6.6l2.2-2.2a1 1 0 0 1 1-.25 11.4 11.4 0 0 0 3.6.57 1 1 0 0 1 1 1V20a1 1 0 0 1-1 1A17 17 0 0 1 3 4a1 1 0 0 1 1-1h3.5a1 1 0 0 1 1 1c0 1.25.2 2.45.57 3.57a1 1 0 0 1-.25 1z"/></svg>555-014-2290</li>
    <li><svg width="16" height="12" viewBox="0 0 16 12" fill="var(--gold)"><path d="M0 0h16v12H0zM1.5 1.5 8 6.5l6.5-5"/><path d="M1.5 1.5 8 6.5l6.5-5" fill="none" stroke="#fff" stroke-width="1.4"/></svg>info@larkfieldrecordrelief.com</li>
  </ul>
  <div class="footer-rule"></div>
  <p class="copyright">©2023 Larkfield Record Relief. All rights reserved.</p>
  <span class="social" aria-label="Social profile" style="left:927px"></span>
  <span class="social" aria-label="Social profile" style="left:982px"></span>
  <span class="social" aria-label="Social profile" style="left:1039px"></span>
</footer>

</body>
</html>
```